Website Design for Business Law Firm

We have a logo and now we would like a web site design for our new website. Our small firm provides creative and aggressive transactional (not litigation) legal services to advise healthcare, technology, internet-based and traditional companies and investors in such companies on healthcare, technology, financing, mergers/acquisitions, real estate and other transactions, legal compliance and general corporate and business matters.

We would like to see a website design that is professional and appropriate for executives, professionals, investors and government regulators to visit, that conveys professionalism and competence while being a little edgy and modern - no typical legal motifs such as gavels, books, or scales of justice. We advise businesses and investors and guide them through complicated issues quickly, capably and differently from other law firms. We are part of the business team and get things done.

The logo is attached, and we like gray as a color to complement it. The intention of the logo is to convey that in a storm or challenging time, people come to this firm, and people come to this firm when they need the power and disruption to change things or shake them up.

I have also enclosed a picture of our business card for consideration.

On the other hand, you can check out the current simple site at www.venhollow.example to see we have used a space motif in the past to evoke that we help create stars (the nebula featured there). This is not a necessary part of the new website and it may look better without it.

We appreciate your creativity and look forward to designs.

Industry/Entity Type

Business

Requirements
Must have
• We anticipate the following pages, and you may submit different ideas for the different pages:
• 1. Landing page
• 2. Services pages - healthcare, IT/Technology, general counsel services, financings, mergers/acquisitions, mediation/arbitration, procurement and productization
• 3. About Us including contact information
• Our name and contact information:
• Quellane Law Firm, P.C.
• 8716 SW 19th Ave.
• Portland, OR 97213
• phone: 971.555.0143
• fax: 971.555.0187
Nice to have
• Please consider designs that enhance the impressions we are looking for
Should not have
• Please no gavels, scales of justice, law books, or similar traditional legal imagery.

```html
<!DOCTYPE html>
<html lang="en">
<head>
<meta charset="utf-8">
<title>Quellane Law Firm, P.C.</title>
<link href="https://fonts.googleapis.com/css2?family=Michroma&family=PT+Sans&family=Ubuntu:wght@300;400&display=swap" rel="stylesheet">
<style>
:root{
  --band:#4b4b4b;
  --band-light:#6a6a6a;
  --white:#ffffff;
  --ink:#3a3a3a;
  --muted:#8c8c8c;
  --teal:#4f7a7a;
  --panel:rgba(62,62,62,0.88);
}
*{margin:0;padding:0;box-sizing:border-box}
html,body{width:1187px;height:1200px;overflow:hidden;background:var(--white)}
.page{position:relative;width:1187px;height:1200px;font-family:'PT Sans',sans-serif}
.site-header{position:absolute;left:0;top:0;width:1187px;height:115px;background:var(--band)}
.brand{position:absolute;left:110px;top:22px;width:287px;text-align:center;color:var(--white);font-family:'Michroma',sans-serif}
.brand-mark{display:flex;align-items:center;justify-content:center;gap:10px;font-size:30px;letter-spacing:4px;height:48px}
.brand-mark i{width:14px;height:14px;background:var(--teal);display:block}
.brand-sub{font-size:15px;letter-spacing:3px;margin-top:14px}
.header-contact{position:absolute;left:850px;top:20px;color:#e4e4e4;font-family:'Michroma',sans-serif;font-size:13px;letter-spacing:3px;white-space:nowrap}
.header-contact p{display:flex;align-items:center;gap:10px;height:28px}
.header-nav{position:absolute;left:815px;top:90px;width:272px;height:25px;background:var(--band-light);clip-path:polygon(12px 0,calc(100% - 12px) 0,100% 100%,0 100%);display:flex;justify-content:center;gap:16px;align-items:center;font-size:14px;color:#eee}
.hero{position:absolute;left:0;top:115px;width:1187px;height:465px;background:linear-gradient(90deg,#e8e8e8 0%,#c9c9c9 20%,#dadada 45%,#a9a9a9 70%,#cfcfcf 90%,#f1f1f1 100%)}
.hero-title{position:absolute;right:102px;top:92px;text-align:right;font-family:'Michroma',sans-serif;color:#3d3d3d;font-size:36px;line-height:60px;letter-spacing:6px;white-space:nowrap}
.hero-panel{position:absolute;left:628px;top:221px;width:459px;min-height:155px;background:var(--panel);color:var(--white);font-family:'Michroma',sans-serif;font-size:9px;line-height:19px;letter-spacing:0.8px;text-transform:uppercase;text-align:right;padding:8px 10px;white-space:nowrap}
.hero-panel p+p{margin-top:17px}
.slider-dots{position:absolute;left:481px;top:443px;display:flex;gap:6px}
.slider-dots span{width:61px;height:4px;background:#555}
.slider-dots .active{background:var(--teal)}
.hero-shade{position:absolute;left:0;top:560px;width:1187px;height:30px;background:radial-gradient(ellipse 55% 100% at 50% 0%,rgba(0,0,0,.35),rgba(0,0,0,0) 70%)}
.services-heading{position:absolute;left:163px;top:612px;width:855px;text-align:center;font-family:'Michroma',sans-serif;font-weight:400;color:var(--teal);font-size:15px;letter-spacing:2.4px;white-space:nowrap;line-height:20px}
.rule{position:absolute;left:165px;top:648px;width:851px;border-top:1px dotted #777}
.service{position:absolute;display:flex;align-items:flex-start;gap:9px;font-family:'Ubuntu',sans-serif;font-weight:300;font-size:15px;line-height:22px;color:var(--muted);white-space:nowrap}
.service svg{flex:none;margin-top:-3px}
.contact{position:absolute;left:0;top:960px;width:1187px;height:180px;background:var(--band);color:var(--white)}
.contact-shade{position:absolute;left:0;top:920px;width:1187px;height:40px;background:radial-gradient(ellipse 50% 100% at 50% 100%,rgba(0,0,0,.35),rgba(0,0,0,0) 70%)}
.contact h2{position:absolute;left:0;top:22px;width:100%;text-align:center;font-family:'Michroma',sans-serif;font-weight:400;font-size:16px;letter-spacing:3px;font-variant:small-caps}
.contact-item{position:absolute;top:71px;display:flex;gap:8px;align-items:flex-start;font-size:16px;line-height:21px;white-space:nowrap}
.copyright{position:absolute;left:0;top:1160px;width:100%;text-align:center;font-size:13px;color:var(--ink)}
</style>
</head>
<body>
<div class="page">
  <header class="site-header">
    <div class="brand">
      <div class="brand-mark"><i></i>QUELLANE</div>
      <div class="brand-sub">LAW FIRM</div>
    </div>
    <div class="header-contact">
      <p><svg width="16" height="14" viewBox="0 0 16 14"><path d="M1 5 Q8 -1 15 5 L12 6 L11 4 Q8 3 5 4 L4 6Z" fill="#ddd"/><rect x="4" y="7" width="8" height="6" rx="1" fill="#ddd"/></svg>Tel: 971.555.0143</p>
      <p><svg width="16" height="14" viewBox="0 0 16 14"><rect x="4" y="1" width="8" height="5" fill="none" stroke="#ddd"/><rect x="1" y="6" width="14" height="7" rx="1" fill="#ddd"/></svg>Fax: 971.555.0187</p>
    </div>
    <nav class="header-nav"><span>For lawyers</span><span>Sign in</span><span>Register</span></nav>
  </header>

  <section class="hero" role="img" aria-label="Smiling lawyer in a light suit and striped tie, colleagues in a bright office behind">
    <div class="hero-title">QUELLANE<br>LAW FIRM,P.C</div>
    <div class="hero-panel">
      <p>Lorem ipsum dolor sit amet, consectetuer adipiscing<br>elit, sed diam nonummy nibh euismod tincidunt ut<br>laoreet dolore magna aliquam erat volutpat.</p>
      <p>Ut wisi enim ad minim veniam, quis nostrud exerci<br>tation ullamcorper suscipit lobortis nisl ut aliquip<br>ex ea commodo consequat.</p>
    </div>
    <div class="slider-dots"><span></span><span class="active"></span><span></span></div>
  </section>
  <div class="hero-shade"></div>

  <h1 class="services-heading">PRAGMATIC,CREATIVE SERVICES FOR INNOVATIVE BUSINESSES</h1>
  <div class="rule"></div>

  <svg width="0" height="0" style="position:absolute"><defs><symbol id="arrow-ico" viewBox="0 0 32 32"><path d="M24 6 A13 13 0 1 0 24 26" fill="none" stroke="#6f8a8a" stroke-width="1.5"/><path d="M7 16 H27 M20 9 L27 16 L20 23" fill="none" stroke="#3f5f5f" stroke-width="2"/></symbol></defs></svg>

  <div class="service" style="left:165px;top:681px"><svg width="32" height="32"><use href="#arrow-ico"/></svg>Outsourcing</div>
  <div class="service" style="left:165px;top:719px"><svg width="32" height="32"><use href="#arrow-ico"/></svg>Venture Financing</div>
  <div class="service" style="left:165px;top:757px"><svg width="32" height="32"><use href="#arrow-ico"/></svg>Stragtegic Alliances</div>
  <div class="service" style="left:165px;top:796px"><svg width="32" height="32"><use href="#arrow-ico"/></svg>Procurements-Buying or selling</div>
  <div class="service" style="left:165px;top:838px"><svg width="32" height="32"><use href="#arrow-ico"/></svg>Venture Formation and startup</div>
  <div class="service" style="left:165px;top:875px"><svg width="32" height="32"><use href="#arrow-ico"/></svg>Licensing and Technology Exploitation</div>

  <div class="service" style="left:496px;top:682px"><svg width="32" height="32"><use href="#arrow-ico"/></svg>Contracts</div>
  <div class="service" style="left:496px;top:721px"><svg width="32" height="32"><use href="#arrow-ico"/></svg>Real Estate</div>
  <div class="service" style="left:496px;top:758px"><svg width="32" height="32"><use href="#arrow-ico"/></svg>Dispute Resolution</div>
  <div class="service" style="left:496px;top:797px"><svg width="32" height="32"><use href="#arrow-ico"/></svg>Audits,Analyses and legal<br>project management</div>
  <div class="service" style="left:496px;top:848px"><svg width="32" height="32"><use href="#arrow-ico"/></svg>Creative Private Financing<br>Arrangements</div>

  <div class="service" style="left:764px;top:681px"><svg width="32" height="32"><use href="#arrow-ico"/></svg>Mergers and Acquisitions</div>
  <div class="service" style="left:764px;top:721px"><svg width="32" height="32"><use href="#arrow-ico"/></svg>Businesses Relationships</div>
  <div class="service" style="left:764px;top:761px"><svg width="32" height="32"><use href="#arrow-ico"/></svg>Service as a Mediator or Arbitrator</div>
  <div class="service" style="left:767px;top:802px"><svg width="32" height="32"><use href="#arrow-ico"/></svg>Vandor Management</div>
  <div class="service" style="left:767px;top:840px"><svg width="32" height="32"><use href="#arrow-ico"/></svg>Local Counsel for Transactions<br>and dueDiligence</div>

  <div class="contact-shade"></div>
  <footer class="contact">
    <h2>Contact us</h2>
    <div class="contact-item" style="left:148px"><svg width="18" height="24" viewBox="0 0 18 24"><path d="M9 23 C3 15 1 12 1 9 A8 8 0 0 1 17 9 C17 12 15 15 9 23Z" fill="none" stroke="#fff" stroke-width="1.3"/><circle cx="9" cy="9" r="3" fill="none" stroke="#fff" stroke-width="1.3"/></svg><span>Quellane Law Firm,p.c<br>P.O.Box 5530,Portland,OR 97213</span></div>
    <div class="contact-item" style="left:455px;top:76px"><svg width="17" height="14" viewBox="0 0 17 14"><path d="M1 5 L8.5 1 L16 5 V13 H1Z" fill="#ddd"/><path d="M1 5 L8.5 10 L16 5" fill="none" stroke="#4b4b4b"/></svg><span>info@quellane.example</span></div>
    <div class="contact-item" style="left:672px;top:76px"><svg width="16" height="14" viewBox="0 0 16 14"><path d="M1 5 Q8 -1 15 5 L12 6 L11 4 Q8 3 5 4 L4 6Z" fill="#ddd"/><rect x="4" y="7" width="8" height="6" rx="1" fill="#ddd"/></svg><span>Tel: 971.555.0143</span></div>
    <div class="contact-item" style="left:877px;top:76px"><svg width="16" height="14" viewBox="0 0 16 14"><rect x="4" y="1" width="8" height="5" fill="none" stroke="#ddd"/><rect x="1" y="6" width="14" height="7" rx="1" fill="#ddd"/></svg><span>fax: 971.555.0187</span></div>
  </footer>

  <p class="copyright">Copyright © 2013 Quellane Law Firm,p.c All rights reserved.</p>
</div>
</body>
</html>
```